RESIDENTIAL CONSTRUCTION

We are a company that specializes in building custom residential homes, the design should also emphasize that quality and service is our priority.

Industry/Entity Type

Construction Company

Contact Information for Business Card

Contact Person: Tobias Lindqvar
Company Address: 463 Westbrook Ave San Jose , Ca 95112
Phone Number : 408-731-2946
Email Address: Oakfieldcrafters731@mailvessel.net

Font styles to use
Sans Serif

Colors
ec1f27

Requirements
Must have
• CSLB # 7362519
Nice to have
• needs to have same color as logo i uploaded, we will be printing these on a clear plastic card.

```html
<!DOCTYPE html>
<html lang="en">
<head>
<meta charset="utf-8">
<title>Oakfield Crafters – Business Card</title>
<link rel="stylesheet" href="https://fonts.googleapis.com/css2?family=Oswald:wght@500;600&family=Open+Sans:wght@400&display=swap">
<style>
  :root{
    --backdrop:#2a2a2a;
    --card:#1c1c1d;
    --red:#ec1f27;
    --white:#f2f2f2;
    --muted:#d8d8d8;
  }
  *{box-sizing:border-box;margin:0;padding:0}
  html,body{width:1200px;height:900px;overflow:hidden;background:var(--backdrop)}
  .canvas{width:1200px;height:900px;display:flex;flex-direction:column;align-items:center;justify-content:center;gap:44px}
  .card{position:relative;width:640px;height:366px;background:var(--card);border-radius:3px}
  .brand{display:flex;align-items:center;gap:12px;font-family:"Oswald",sans-serif;font-weight:600;color:var(--red);text-transform:uppercase;letter-spacing:1px;white-space:nowrap}
  .brand-mark{background:var(--red);flex:none}
  .card-front{display:flex;align-items:center;justify-content:center}
  .card-front .brand{font-size:48px}
  .card-front .brand-mark{width:28px;height:28px}
  .card-back .brand{position:absolute;top:56px;right:48px;font-size:30px;gap:9px}
  .card-back .brand-mark{width:18px;height:18px}
  .holder{position:absolute;top:40px;left:48px}
  .holder-name{font-family:"Oswald",sans-serif;font-weight:600;font-size:28px;color:var(--white);text-transform:uppercase;letter-spacing:.3px;line-height:1.1}
  .holder-role{font-family:"Oswald",sans-serif;font-weight:500;font-style:italic;font-size:16px;color:var(--red);text-transform:uppercase;margin-top:2px}
  .holder-rule{width:72px;height:2px;background:var(--red);margin-top:10px}
  .contact{position:absolute;left:48px;bottom:52px;list-style:none;font-family:"Open Sans",sans-serif;font-size:16px;color:var(--muted)}
  .contact li{display:flex;align-items:center;gap:12px;line-height:28px}
  .contact svg{width:14px;height:14px;fill:var(--red);flex:none}
</style>
</head>
<body>
<main class="canvas">
  <section class="card card-front">
    <div class="brand"><span class="brand-mark"></span>Oakfield Crafters</div>
  </section>

  <section class="card card-back">
    <div class="holder">
      <h1 class="holder-name">Tobias Lindqvar</h1>
      <p class="holder-role">Job Title I CSLB # 7362519</p>
      <div class="holder-rule"></div>
    </div>
    <div class="brand"><span class="brand-mark"></span>Oakfield Crafters</div>
    <ul class="contact">
      <li><svg viewBox="0 0 24 24"><path d="M6.6 10.8a15 15 0 0 0 6.6 6.6l2.2-2.2a1 1 0 0 1 1-.25 11.4 11.4 0 0 0 3.6.57 1 1 0 0 1 1 1V20a1 1 0 0 1-1 1A17 17 0 0 1 3 4a1 1 0 0 1 1-1h3.5a1 1 0 0 1 1 1c0 1.25.2 2.45.57 3.57a1 1 0 0 1-.25 1z"/></svg>408-731-2946</li>
      <li><svg viewBox="0 0 24 24"><path d="M2 5h20v14H2z M2 5l10 8 10-8" /><path d="M2 5h20L12 13z" fill="#1c1c1d"/></svg>Oakfieldcrafters731@mailvessel.net</li>
      <li><svg viewBox="0 0 24 24"><path d="M12 2a7 7 0 0 0-7 7c0 5.2 7 13 7 13s7-7.8 7-13a7 7 0 0 0-7-7zm0 9.5A2.5 2.5 0 1 1 12 6.5a2.5 2.5 0 0 1 0 5z"/></svg>463 Westbrook Ave San Jose , Ca 95112</li>
    </ul>
  </section>
</main>
</body>
</html>
```